Verdalunex webpage design

We are offering eco/sustainable theme vacations and make them bookable via our site. Our reference site is www.voyelmora.com. We want something similar but with a bit more creativity and elegant design. In our colors, which would depend on our logo colors.

NB: WE ARE NOT ASKING FOR A FULL BLOWN SITE. WE NEED 2 PAGE DESIGN FOR THE FIRST IMPRESSION. AFTER THAT WE CREATE A BUDGET FOR COMPLETION OF THE PROJECT.

Target Market(s)

Eco/Sustainable tourism.

Industry/Entity Type

Tourism

Coding

Coded - Design and coding required

Number of Pages Required

2 page

Requirements
Must have
• Reference site is voyelmora.com. But be creative and design something a bit different and more beautiful.
• NB: WE ARE NOT ASKING FOR A FULL BLOWN SITE. WE NEED 2 PAGE DESIGN FOR THE FIRST IMPRESSION. AFTER THAT WE CREATE A BUDGET FOR COMPLETION OF THE PROJECT.
• Please see our logo.

```html
<!DOCTYPE html>
<html lang="en">
<head>
<meta charset="utf-8">
<title>Verdalunex — Travel Differently</title>
<link rel="stylesheet" href="https://fonts.googleapis.com/css2?family=Playfair+Display:ital,wght@1,700;1,900&family=Roboto:wght@300;400;500;700&display=swap">
<style>
:root{
  --blue:#12a6f2;
  --green:#36d57a;
  --grad:linear-gradient(90deg,var(--blue),var(--green));
  --ink:#2b2b2b;
  --muted:#8a8a8a;
  --line:#d9d9d9;
  --sand:#f8f5f0;
  --footer:#333334;
  --footer-text:#a9a9a9;
  --promo-green:#3ad14f;
}
*{box-sizing:border-box;margin:0;padding:0}
html,body{width:1200px;height:3314px;overflow:hidden}
body{font-family:"Roboto",sans-serif;color:var(--ink);background:#fff;position:relative}
section,header,footer{display:flow-root;overflow:hidden}
.serif{font-family:"Playfair Display",serif;font-style:italic;font-weight:900}
.btn{display:inline-flex;align-items:center;justify-content:center;gap:6px;background:var(--grad);color:#fff;border-radius:20px;font-size:14px;border:none;font-family:"Roboto",sans-serif}
.wrap{width:734px;margin:0 auto;position:relative}
.brand{display:flex;align-items:center;gap:5px;font-family:"Roboto",sans-serif;font-weight:700;font-size:19px;color:#1f1f1f}
.brand-dot{width:18px;height:18px;border-radius:50%;background:var(--blue)}

/* nav */
.nav{height:40px;display:flex;align-items:center;justify-content:space-between;padding:0 230px 0 232px;font-size:12px;color:#555}
.nav-links{display:flex;align-items:center;gap:30px}
.nav-links span{display:flex;align-items:center;gap:5px}
.nav .btn{width:92px;height:25px;font-size:12px}

/* hero */
.hero{height:635px;position:relative;background:linear-gradient(180deg,#6d8579 0%,#3f6a4a 25%,#466d52 45%,#3aa0a6 58%,#3f8c86 66%,#6f9a48 78%,#5d8a3a 100%);text-align:center;color:#fff}
.hero h1{font-size:60px;padding-top:240px;letter-spacing:.5px;line-height:1.2}
.hero p{font-size:13px;margin-top:6px}
.hero .btn{width:125px;height:33px;margin-top:24px;font-size:14px}

/* section illustration placeholder */
.section-icon{width:78px;height:78px;margin:0 auto;border-radius:50%;background:radial-gradient(circle at 40% 35%,#e7f3ec,#cfe6da)}
.section-title{font-size:29px;text-align:center;line-height:1.3}
.section-sub{font-size:11px;color:var(--muted);text-align:center}

/* search */
.search{height:375px;border:1px solid #ead8d4;border-top:none;text-align:center;padding-top:54px}
.search .section-title{margin-top:34px}
.search .section-sub{margin-top:12px}
.filters{display:flex;gap:17px;justify-content:center;margin-top:32px}
.filter{width:108px;height:34px;border:1px solid #cfcfcf;border-radius:18px;display:flex;align-items:center;justify-content:center;gap:6px;font-size:11px;color:#9a9a9a}
.filters .btn{width:106px;height:34px}

/* offers */
.offers{height:635px;background:var(--sand);text-align:center;padding-top:64px}
.offers .section-icon{background:radial-gradient(circle at 40% 35%,#fbeedb,#f1dcc0)}
.offers .section-title{margin-top:26px}
.cards{display:flex;gap:28px;justify-content:center;margin-top:36px}
.card{width:225px;height:297px;background:#fff;text-align:left}
.card-img{height:168px}
.card-body{padding:12px 13px 0}
.card-head{display:flex;justify-content:space-between;align-items:baseline}
.card-head h3{font-size:13px}
.card-head span{font-size:13px;color:#888}
.card-body p{font-size:9.5px;color:#8d8d8d;line-height:1.8;margin-top:6px;padding-bottom:10px;border-bottom:1px solid var(--line)}
.card-meta{display:flex;align-items:center;font-size:9.5px;color:#777;margin-top:10px;gap:14px}
.card-meta .stars{margin-left:auto;color:#f3b62b;letter-spacing:1px;font-size:11px}
.stars .off{color:#bdbdbd}
.offers .btn{width:138px;height:33px;margin-top:30px;font-size:13px}

/* destinations */
.dest{height:604px;text-align:center;padding-top:64px}
.dest .section-icon{background:radial-gradient(circle at 40% 35%,#fde3da,#f6c9b8)}
.dest .section-title{margin-top:36px}
.dest .section-sub{margin-top:12px}
.tiles{display:flex;gap:18px;justify-content:center;margin-top:42px}
.tile{width:169px;height:238px;position:relative;color:#fff;display:flex;flex-direction:column;justify-content:flex-end;padding-bottom:18px}
.tile h4{font-size:13px}
.tile span{font-size:9.5px;margin-top:4px}

/* promo */
.promo{height:435px;background:linear-gradient(90deg,#4c5a4c 0%,#6d7a70 30%,#3e5c52 55%,#1f6e63 75%,#2f5d4a 100%);text-align:center;color:#fff}
.promo .off-tag{font-size:50px;color:var(--promo-green);padding-top:84px;line-height:1}
.promo h2{font-size:25px;margin-top:14px}
.promo p{font-size:16px;line-height:1.35;width:500px;margin:18px auto 0}
.promo .btn{width:138px;height:33px;margin-top:52px;font-size:13px}

/* updates */
.updates{height:250px;background:var(--sand);text-align:center}
.updates h2{font-size:29px;padding-top:48px;line-height:1.3}
.updates p{font-size:10.5px;color:var(--muted);line-height:1.7;margin-top:10px}
.signup{width:382px;height:34px;margin:20px auto 0;border:1px solid #b9b9b9;border-radius:18px;display:flex;align-items:center;justify-content:space-between;padding-left:16px;font-size:10.5px;color:#8d8d8d}
.signup .btn{width:94px;height:34px;margin-right:-1px;font-size:11px}

/* footer */
.footer{height:340px;background:var(--footer);color:var(--footer-text);padding-top:60px}
.footer-cols{display:flex}
.footer .brand{color:#fff}
.footer .col-about{width:282px}
.footer .col-about p{font-size:10.5px;line-height:1.7;margin-top:14px;width:222px}
.follow{display:flex;align-items:center;gap:8px;margin-top:16px;font-size:10px;color:#fff}
.follow i{width:28px;height:28px;border-radius:50%;background:#666;display:inline-block}
.follow b{font-weight:400;margin-right:6px}
.col-map{width:157px}
.footer h5{font-size:12px;color:#fff;font-weight:500;margin-top:4px}
.footer ul{list-style:none;font-size:10.5px;line-height:1.7;margin-top:14px}
.contact li{display:flex;gap:8px}
.contact svg{flex:none;margin-top:4px}
.footer-bottom{border-top:1px solid #6a6a6a;margin-top:32px;padding-top:26px;font-size:10.5px}
</style>
</head>
<body>

<header class="nav">
  <div class="brand"><span class="brand-dot"></span>Verdalunex</div>
  <nav class="nav-links">
    <span>Tours</span>
    <span><svg width="10" height="8" viewBox="0 0 10 8"><path d="M1 2l4 4 4-4" fill="none" stroke="#2aa85a" stroke-width="1.4"/></svg>USD</span>
    <span><svg width="14" height="13" viewBox="0 0 24 22"><path d="M12 20s-9-5.5-9-11.5A5 5 0 0 1 12 6a5 5 0 0 1 9 2.5C21 14.5 12 20 12 20z" fill="none" stroke="#2bc06a" stroke-width="2"/></svg>Favorites</span>
    <span>Partners</span>
    <span>Log in</span>
    <a class="btn"><svg width="11" height="11" viewBox="0 0 12 12"><circle cx="6" cy="4" r="2.5" fill="none" stroke="#fff"/><path d="M1.5 11.5c0-3 2-4.5 4.5-4.5s4.5 1.5 4.5 4.5" fill="none" stroke="#fff"/></svg>Sign up</a>
  </nav>
</header>

<section class="hero" role="img" aria-label="Traveller seated on a log beside a turquoise mountain lake surrounded by pine forest">
  <h1 class="serif">Travel Differently</h1>
  <p>Visiting protected areas intended as low impact and environmentally sustainable.</p>
  <a class="btn">Book a Tour</a>
</section>

<section class="search">
  <div class="section-icon" role="img" aria-label="Illustration of a globe with map pins"></div>
  <h2 class="section-title serif">Search Our Offers</h2>
  <p class="section-sub">Lorem ipsum dolor sit amet, consectetuer adipiscing elit, sed diam.</p>
  <div class="filters">
    <div class="filter">⌄ Country</div>
    <div class="filter">⌄ Date</div>
    <div class="filter">⌄ Duration</div>
    <div class="filter">⌄ Min Price</div>
    <div class="filter">⌄ Max Price</div>
    <a class="btn"><svg width="13" height="13" viewBox="0 0 14 14"><circle cx="6" cy="6" r="4.5" fill="none" stroke="#fff" stroke-width="1.5"/><path d="M9.5 9.5L13 13" stroke="#fff" stroke-width="1.5"/></svg>Search</a>
  </div>
</section>

<section class="offers">
  <div class="section-icon" role="img" aria-label="Illustration of a beach umbrella and sun lounger"></div>
  <h2 class="section-title serif">Special Offers</h2>
  <div class="cards">
    <article class="card">
      <div class="card-img" role="img" aria-label="Golden pagodas on a hill at sunset in Chiang Mai" style="background:linear-gradient(180deg,#5f7fa8,#c89a5c 55%,#4f6b3a)"></div>
      <div class="card-body">
        <div class="card-head"><h3 class="serif">Chang Mai, Thailand</h3><span>$1435</span></div>
        <p>Lorem ipsum dolor sit amet, consectetuer adipiscing elit, sed diam nonummy nibh.</p>
        <div class="card-meta"><span>▭ 10 Days</span><span>⚲ 2+</span><span class="stars"><span class="off">★</span>★★★★</span></div>
      </div>
    </article>
    <article class="card">
      <div class="card-img" role="img" aria-label="Stone bridge and castle on the Loire river" style="background:linear-gradient(180deg,#a9c4de,#c8c6bc 50%,#5d7f8f)"></div>
      <div class="card-body">
        <div class="card-head"><h3 class="serif">Loire Castles, France</h3><span>$2350</span></div>
        <p>Lorem ipsum dolor sit amet, consectetuer adipiscing elit, sed diam nonummy nibh.</p>
        <div class="card-meta"><span>▭ 12 Days</span><span>⚲ 4+</span><span class="stars"><span class="off">★★</span>★★★</span></div>
      </div>
    </article>
    <article class="card">
      <div class="card-img" role="img" aria-label="Limestone islands and junk boat in Ha Long Bay" style="background:linear-gradient(180deg,#d6e8ec,#3e8a4f 45%,#1f9aa0)"></div>
      <div class="card-body">
        <div class="card-head"><h3 class="serif">Ha Long Bay, Vietnam</h3><span>$1654</span></div>
        <p>Lorem ipsum dolor sit amet, consectetuer adipiscing elit, sed diam nonummy nibh.</p>
        <div class="card-meta"><span>▭ 8 Days</span><span>⚲ 3+</span><span class="stars">★★★★★</span></div>
      </div>
    </article>
  </div>
  <a class="btn">View All Tours</a>
</section>

<section class="dest">
  <div class="section-icon" role="img" aria-label="Illustration of a travel backpack"></div>
  <h2 class="section-title serif">Popular Destinations</h2>
  <p class="section-sub">Lorem ipsum dolor sit amet, consectetuer adipiscing elit, sed diam.</p>
  <div class="tiles">
    <div class="tile" role="img" aria-label="Singapore waterfront skyline at dusk" style="background:linear-gradient(180deg,#7f93b8,#d9a08a 50%,#3c4a66)"><h4 class="serif">Singapore</h4><span>Starting $450</span></div>
    <div class="tile" role="img" aria-label="Sydney harbour with bridge and boats" style="background:linear-gradient(180deg,#6a6f96,#4d6f8a 50%,#2c4a5e)"><h4 class="serif">Sydney, Australia</h4><span>Starting $650</span></div>
    <div class="tile" role="img" aria-label="Madrid rooftops at sunset" style="background:linear-gradient(180deg,#c78a55,#b56c3f 50%,#5e3b2a)"><h4 class="serif">Madrid, Spain</h4><span>Starting $1350</span></div>
    <div class="tile" role="img" aria-label="Illuminated temple in Penang at night" style="background:linear-gradient(180deg,#1d2a58,#3a3f7a 50%,#1a1b3c)"><h4 class="serif">Penang, Malaysia</h4><span>Starting $650</span></div>
  </div>
</section>

<section class="promo" role="img" aria-label="Traveller sitting in a long-tail boat on emerald water near Koh Phai Island">
  <div class="off-tag serif">20% Off</div>
  <h2 class="serif">Koh Phai Island, Thailand</h2>
  <p>Special limited time promotion. Lorem ipsum dolor sit amet, consectetuer adipiscing elit, sed diam nonummy nibh euismod tincidunt ut laoreet dolore magna aliquam erat volutpat.</p>
  <a class="btn">Book This Tour</a>
</section>

<section class="updates">
  <h2 class="serif">Get Regular Updates</h2>
  <p>Lorem ipsum dolor sit amet, consectetuer adipiscing elit, sed diam nonummy nibh euismod<br>tincidunt ut laoreet dolore magna aliquam erat volutpat. Ut wisi enim ad minim veniam.</p>
  <div class="signup"><span>Enter your email</span><a class="btn">Subscribe</a></div>
</section>

<footer class="footer">
  <div class="wrap">
    <div class="footer-cols">
      <div class="col-about">
        <div class="brand"><span class="brand-dot"></span>Verdalunex</div>
        <p>Lorem ipsum dolor sit amet, consectetuer adipiscing elit, sed diam nonummy nibh euismod tincidunt ut laoreet dolore magna aliquam erat volutpat.</p>
        <div class="follow"><b>FOLLOW US</b><i></i><i></i><i></i><i></i></div>
      </div>
      <div class="col-map">
        <h5>SITEMAP</h5>
        <ul><li>Our Philosophy</li><li>Mission Statement</li><li>Tours</li><li>Partners</li><li>Log In</li></ul>
      </div>
      <div class="col-contact">
        <h5>CONTACT US</h5>
        <ul class="contact">
          <li><svg width="10" height="10" viewBox="0 0 10 10"><path d="M2 1l2 2-1 1.5a6 6 0 0 0 2.5 2.5L7 6l2 2-1.5 1.5C4 9 1 6 .5 2.5z" fill="none" stroke="#a9a9a9" stroke-width=".9"/></svg>+44 20 5550 1234</li>
          <li><svg width="10" height="10" viewBox="0 0 10 10"><rect x=".5" y="2" width="9" height="6" fill="none" stroke="#a9a9a9" stroke-width=".9"/><path d="M.5 2l4.5 3.5L9.5 2" fill="none" stroke="#a9a9a9" stroke-width=".9"/></svg>info@verdalunex.com</li>
          <li><svg width="10" height="10" viewBox="0 0 10 10"><path d="M5 9.5S1.5 6 1.5 4a3.5 3.5 0 0 1 7 0C8.5 6 5 9.5 5 9.5z" fill="none" stroke="#a9a9a9" stroke-width=".9"/><circle cx="5" cy="4" r="1.2" fill="#a9a9a9"/></svg><span>12 Alder Row,<br>Fernhill, Lakeford<br>LF4 2QX, UK</span></li>
        </ul>
      </div>
    </div>
    <div class="footer-bottom">Terms &amp; Conditions &nbsp;|&nbsp; Privacy Policy &nbsp;|&nbsp; Copyright © 2019 Verdalunex.</div>
  </div>
</footer>

</body>
</html>
```